Corlath Landscaping - WebSite
I like the rounded edges like in draft #18 and #20. Also like the use of the logo's in #20. I like the menu bars in #18 too.
Can you guys add a "Pay Now" graphic. It doesn't need to be those exact words, but I'd like to be able to send users to the site and click on that link to pay a one time bill or signup for AutoPay. Thanks!!!
Hey guys. Thanks for submitting the drafts. They look great.
I have been so busy that I have just been able to take a quick look. I haven't gotten a chance to provide feedback and answer questions. I need to extend the contest. I'll provide feedback tomorrow. Thanks!!!

```html
<!DOCTYPE html>
<html lang="en">
<head>
<meta charset="utf-8">
<title>Corlath Landscaping</title>
<link href="https://fonts.googleapis.com/css2?family=Arimo:wght@400;700&family=Cinzel:wght@700&display=swap" rel="stylesheet">
<style>
  :root{
    --bg-top:#eef3e2;
    --bg-mid:#f6f1b8;
    --bg-bottom:#f7de3a;
    --green-dark:#1d4409;
    --green:#2c6410;
    --green-panel:#356f15;
    --green-light:#5f9b2a;
    --yellow:#f4d53a;
    --yellow-soft:#fbe98a;
    --white:#ffffff;
    --text-light:#eaf3d8;
    --field:#e9ecdf;
  }
  *{margin:0;padding:0;box-sizing:border-box}
  html,body{width:1200px;height:1086px;overflow:hidden}
  body{
    position:relative;
    font-family:"Arimo",Arial,sans-serif;
    background:linear-gradient(180deg,var(--bg-top) 0%,var(--bg-top) 30%,var(--bg-mid) 70%,var(--bg-bottom) 100%);
  }
  .brand{position:absolute;left:160px;top:40px;display:flex;align-items:center;gap:14px}
  .brand-dot{width:34px;height:34px;border-radius:50%;background:var(--green)}
  .brand-name{font-family:"Cinzel",serif;font-weight:700;font-size:30px;line-height:1.05;color:var(--green-dark)}
  .top-nav{position:absolute;left:716px;top:0;width:346px;height:30px;background:var(--green-dark);border-radius:0 0 16px 16px;display:flex;overflow:hidden}
  .top-nav a{flex:1;text-align:center;color:var(--white);font-size:12px;font-weight:700;line-height:30px;text-decoration:none;letter-spacing:.5px}
  .top-nav a.active{background:var(--yellow);color:var(--white)}
  .pay-now{position:absolute;left:880px;top:54px;height:36px;padding:0 18px 0 12px;display:flex;align-items:center;gap:8px;background:var(--yellow);border:2px solid var(--green-dark);border-radius:18px;color:var(--green-dark);text-decoration:none}
  .pay-now svg{width:18px;height:18px}
  .pay-now strong{font-size:13px;font-weight:700;letter-spacing:.5px}
  .pay-now small{font-size:10px;font-weight:700;opacity:.8}
  .rule{position:absolute;left:0;right:0;top:140px;height:2px;background:var(--green-light);opacity:.5}
  .main-nav{position:absolute;left:470px;top:112px;width:592px;height:30px;background:var(--green-dark);border-radius:16px 16px 0 0;display:flex}
  .main-nav a{flex:1;text-align:center;color:var(--white);font-size:13px;font-weight:700;line-height:30px;text-decoration:none;letter-spacing:.5px}
  .frame{position:absolute;left:147px;top:185px;width:915px;height:720px;background:var(--green);border-radius:28px;overflow:hidden}
  .hero{position:absolute;left:6px;top:8px;width:660px;height:268px;border-radius:22px 0 0 0;background:linear-gradient(135deg,#3f7d1e 0%,#6da33a 40%,#c23a3a 62%,#4a8a22 80%,#2e5e14 100%)}
  .side-info{position:absolute;left:683px;top:8px;width:226px;height:268px;background:var(--green-dark);border-radius:0 22px 0 0;padding:20px 16px;color:var(--text-light)}
  .side-info h3,.col h3{color:var(--yellow);font-size:15px;font-weight:700;letter-spacing:.5px;margin-bottom:6px}
  .side-info p{font-size:13px;line-height:16px;margin-bottom:18px}
  .col{position:absolute;top:285px;height:420px}
  .welcome{left:6px;width:290px;background:var(--green-panel);padding:10px 18px;color:var(--text-light)}
  .welcome p{font-size:13px;line-height:16px;margin-bottom:14px}
  .recent{left:302px;width:364px;background:var(--green-panel);padding:10px 14px}
  .recent-box{background:var(--white);border-radius:6px;padding:12px;height:272px;position:relative}
  .thumbs{display:grid;grid-template-columns:1fr 1fr;gap:8px}
  .thumb{height:100px;border-radius:2px}
  .t1{background:linear-gradient(135deg,#6b9a34,#3d6e1c)}
  .t2{background:linear-gradient(135deg,#c94a6a,#6a9b2e)}
  .t3{background:linear-gradient(135deg,#8a6a48,#4f7d2a)}
  .t4{background:linear-gradient(135deg,#e1c13a,#7a3d8c)}
  .btn{display:inline-block;background:linear-gradient(180deg,var(--green-light),var(--green-dark));color:var(--white);font-size:13px;font-weight:700;border-radius:14px;padding:7px 22px;letter-spacing:.5px;border:2px solid var(--field);text-decoration:none}
  .recent .btn{position:absolute;left:12px;bottom:-14px}
  .quote{left:683px;width:226px;background:var(--green-dark);padding:10px 16px;color:var(--white)}
  .quote label{display:block;font-size:12px;margin:4px 0 3px}
  .field{height:28px;border-radius:14px;background:var(--field);margin-bottom:10px}
  .field.area{height:90px;border-radius:10px}
  .quote .btn{margin-top:4px}
  .quote-brand{position:absolute;left:50%;bottom:30px;transform:translateX(-50%);display:flex;align-items:center;gap:8px;white-space:nowrap}
  .quote-brand .brand-dot{width:20px;height:20px;background:var(--white)}
  .quote-brand span{font-family:"Cinzel",serif;font-weight:700;font-size:15px;line-height:1.1;color:var(--white)}
  .footer{position:absolute;left:0;right:0;top:698px;text-align:center;color:var(--yellow-soft);font-size:11px;font-weight:700}
</style>
</head>
<body>
  <div class="brand"><span class="brand-dot"></span><span class="brand-name">Corlath<br>Landscaping</span></div>

  <nav class="top-nav"><a href="#">HOME</a><a href="#" class="active">TESTIMONIALS</a><a href="#">CONTACT US</a></nav>
  <a class="pay-now" href="#">
    <svg viewBox="0 0 18 18" aria-hidden="true"><rect x="1" y="4" width="16" height="11" rx="2" fill="none" stroke="#1d4409" stroke-width="1.8"/><rect x="1" y="7" width="16" height="2.5" fill="#1d4409"/></svg>
    <strong>PAY NOW</strong><small>BILL / AUTOPAY</small>
  </a>
  <nav class="main-nav"><a href="#">ABOUT US</a><a href="#">MAINTENANCE</a><a href="#">INSTALLATION</a><a href="#">PHOTO GALLERY</a></nav>
  <div class="rule"></div>

  <main class="frame">
    <div class="hero" role="img" aria-label="Photograph of a landscaped garden with flower beds, lawns and winding paths"></div>
    <aside class="side-info">
      <h3>MAINTENANCE</h3>
      <p>Lorem ipsum iusto odio dignissimos ducimus qui blanditiis praesentium voluptatum deleniti atque corrupti quos dolores et quas.</p>
      <h3>INSTALLATION</h3>
      <p>Excepturi sint occaecati cupiditate non provident, similique sunt in culpa qui hardscapes and plants anim, id est laborum et dolorum fuga.</p>
    </aside>

    <section class="col welcome">
      <h3>WELCOME</h3>
      <p>Corlath Landscaping et iusto odio dignissimos ducimus qui blanditiis praesentium voluptatum deleniti atque corrupti quos dolores et quas molestias excepturi sint occaecati cupiditate non provident, similique sunt in culpa qui officia deserunt mollitia animi, id est laborum et dolorum fuga.</p>
      <p>Et harum quidem rerum facilis est et expedita distinctio. Nam libero tempore, cum soluta nobis est eligendi optio cumque nihil impedit quo minus id quod maxime placeat facere possimus, omnis voluptas assumenda est, omnis dolor.</p>
    </section>

    <section class="col recent">
      <h3>RECENT WORK</h3>
      <div class="recent-box">
        <div class="thumbs">
          <div class="thumb t1" role="img" aria-label="Photo of a green lawn and garden"></div>
          <div class="thumb t2" role="img" aria-label="Photo of colourful flower beds"></div>
          <div class="thumb t3" role="img" aria-label="Photo of a planted garden corner"></div>
          <div class="thumb t4" role="img" aria-label="Photo of yellow and purple flowers"></div>
        </div>
        <a class="btn" href="#">VIEW MORE</a>
      </div>
    </section>

    <section class="col quote">
      <h3>BUILD A QUOTE</h3>
      <label>Name</label><div class="field"></div>
      <label>Email</label><div class="field"></div>
      <label>Message</label><div class="field area"></div>
      <a class="btn" href="#">CONTINUE</a>
      <div class="quote-brand"><span class="brand-dot"></span><span>Corlath<br>Landscaping</span></div>
    </section>

    <p class="footer">© 2011 Corlath Landscaping. All Rights Reserved</p>
  </main>
</body>
</html>
```